medical equipment home page redesign

We need a new home page for an existing store. We'll be redoing the entire site to make it more user friendly and follow storybrand guidelines. We have a loose wireframe for the sections, but need help making it look great. The look should be clean, modern, professional, etc. We have a background image we would like to incorporate somewhere because we've just printed business cards and brochures that use this background image. We love parallax effects on backgrounds, so please allow extra big background images so we can utilize that effect. You can find images, etc from our site at brivontel.com. We like the way this site feels: http://okmu.fendaro.com/home/page/venue with the parallax background. And this one, too: https://www.tessilmarow.org/

Target Market(s)

people with chronic pain

Industry/Entity Type

Medical Equipment

Number of Pages Required

1 page

Font styles to use
Sans Serif

Colors
b8a6cd
6b449b
e4daeb

Requirements
Must have
• Please include sections from our wireframe. They don't have to look like the wireframe, but they do need to portray that information in each section.
Nice to have
• It would be great if you could include the background image we have attached
Should not have
• Should not look like the old site.

```html
<!DOCTYPE html>
<html lang="en">
<head>
<meta charset="utf-8">
<title>Brivontel – Light Therapy</title>
<link href="https://fonts.googleapis.com/css2?family=Open+Sans:wght@400;600;700&family=Montserrat:wght@400;600;700&display=swap" rel="stylesheet">
<style>
:root{
  --purple:#6b449b;
  --purple-dark:#4e2f78;
  --lilac:#b8a6cd;
  --mist:#e4daeb;
  --white:#ffffff;
  --ink:#333333;
  --muted:#777777;
  --gold:#f2b500;
  --sun:#f39a2b;
}
*{box-sizing:border-box;margin:0;padding:0}
html,body{width:1200px;height:2636px;overflow:hidden}
body{font-family:"Open Sans",Arial,sans-serif;color:var(--ink);background:var(--white);position:relative}
h2,h3,.brand,.btn,.tab{font-family:"Montserrat",Arial,sans-serif}

/* header */
.site-header{height:88px;display:flex;align-items:center;justify-content:space-between;padding:0 120px;background:var(--white);position:relative;z-index:2}
.brand{display:flex;align-items:center;gap:10px;font-weight:700;font-size:24px;color:var(--purple)}
.brand-dot{width:22px;height:22px;border-radius:50%;background:var(--purple)}
.main-nav{display:flex;gap:36px;align-items:center;font-size:14px;color:var(--ink)}
.btn{display:inline-block;border:2px solid var(--purple);color:var(--purple);padding:8px 20px;font-size:13px;font-weight:600;border-radius:3px;text-transform:uppercase}

/* hero */
.hero{height:184px;position:relative;background:linear-gradient(180deg,#7a4a9e 0%,#c8648a 35%,var(--sun) 70%,#e8a24a 100%);padding:40px 240px 0}
.hero-photo{position:absolute;left:650px;top:10px;width:390px;height:160px;border-radius:8px;background:linear-gradient(120deg,rgba(60,60,70,.55),rgba(120,110,130,.35))}
.hero-copy{position:relative;z-index:1;width:380px}
.hero h1{font-family:"Montserrat",Arial,sans-serif;font-size:24px;color:var(--white);font-weight:700;white-space:nowrap}
.hero p{color:var(--white);font-size:13px;margin:10px 0 16px}
.btn-solid{background:var(--purple);border-color:var(--purple);color:var(--white)}
.tabs{position:absolute;left:240px;right:240px;bottom:-40px;display:flex;height:40px}
.tab{flex:1;background:var(--purple);color:var(--white);display:flex;align-items:center;justify-content:center;font-size:13px;font-weight:600;border-right:1px solid var(--lilac);text-transform:uppercase}
.tab:nth-child(2){background:var(--purple-dark)}
.tab:last-child{border-right:0}

/* sections */
.section-title{text-align:center;font-size:22px;font-weight:700;text-transform:uppercase;color:var(--ink);letter-spacing:.5px}
.how{padding:88px 240px 0;height:368px}
.product-row{display:flex;gap:16px;margin-top:30px;position:relative}
.product{flex:1;text-align:center;font-size:12px}
.product-img{height:110px;border:1px solid var(--mist);background:linear-gradient(135deg,#f4f4f4,#c9c9cf)}
.product-name{margin-top:8px;color:var(--ink)}
.price{color:var(--purple);font-weight:700;margin-top:2px}
.arrow{position:absolute;top:40px;font-size:30px;color:var(--purple)}

.testimonial{height:360px;background:linear-gradient(180deg,var(--purple) 0%,#8a67b4 60%,var(--purple) 100%);padding:30px 0 0;position:relative}
.testimonial .section-title{color:var(--white)}
.quote-card{margin:30px auto 0;width:760px;height:220px;display:flex;position:relative;background:rgba(255,255,255,.12)}
.quote-side{width:200px;background:var(--purple-dark);padding:20px;text-align:center;color:var(--mist);font-size:11px}
.avatar{width:80px;height:80px;border-radius:50%;margin:0 auto 10px;background:linear-gradient(180deg,#c9a98a,#8a6a50)}
.quote-name{color:var(--gold);font-weight:700;font-size:12px}
.quote-text{flex:1;padding:22px 26px;color:var(--white);font-size:12px;line-height:1.6}
.stars{position:absolute;right:24px;bottom:18px;color:var(--gold);font-size:20px;letter-spacing:2px}
.t-arrow{position:absolute;top:120px;color:var(--white);font-size:34px}

.pets{height:380px;padding:70px 240px 0}
.pets .section-title{font-size:28px}
.pets .section-title span{color:var(--purple)}
.pet-photos{display:flex;gap:8px;margin-top:36px;height:220px}
.pet-photos div{border-radius:2px}

.featured{height:340px;background:linear-gradient(180deg,var(--lilac),#9a84b8 55%,var(--lilac));padding:40px 240px 0;position:relative}
.featured .product-row{margin-top:24px}
.featured .product{background:var(--white);padding:6px}
.featured .product-img{height:100px}
.featured .arrow{color:var(--purple-dark)}

.story{height:300px;padding:50px 240px 0;display:flex;gap:30px}
.story-text{flex:1}
.story h3{color:var(--purple);font-size:14px;font-weight:700;text-transform:uppercase;white-space:nowrap}
.story-rule{width:60px;height:2px;background:var(--purple);margin:10px 0 14px}
.story p{font-size:12px;line-height:1.7;color:var(--muted)}
.story-photo{width:360px;height:200px;background:linear-gradient(180deg,#7fa4c8,#6f8a4a 70%,#5a7236)}

.blog{height:340px;background:#f2f2f2;padding:40px 240px 0}
.blog-row{display:flex;gap:16px;margin-top:24px}
.post{flex:1;font-size:11px}
.post-img{height:140px}
.post-meta{color:var(--muted);margin-top:8px;font-size:10px}
.post h4{font-family:"Montserrat",Arial,sans-serif;color:var(--purple);font-size:12px;margin:2px 0 4px;text-transform:uppercase}
.post p{color:var(--muted);line-height:1.5}

.newsletter{height:196px;background:var(--purple);padding:40px 0 0;text-align:center}
.newsletter h2{color:var(--white);font-size:20px;font-weight:600;text-transform:uppercase}
.signup{display:flex;justify-content:center;gap:12px;margin-top:28px}
.field{width:220px;height:34px;background:var(--white);border-radius:2px;font-size:12px;color:var(--muted);text-align:left;padding:9px 12px}
.signup .btn{width:140px;background:var(--purple-dark);color:var(--white);border-color:var(--white);height:34px;padding:0;display:flex;align-items:center;justify-content:center}
.site-footer{height:36px;background:var(--purple-dark);color:var(--mist);font-size:11px;display:flex;align-items:center;padding:0 120px}
</style>
</head>
<body>
<header class="site-header">
  <div class="brand"><span class="brand-dot"></span>Brivontel</div>
  <nav class="main-nav"><span>Home</span><span>Who's Light</span><span>About Us</span><span class="btn">Shop Now</span></nav>
</header>

<section class="hero">
  <div class="hero-photo" role="img" aria-label="Row of handheld light therapy devices glowing in colours"></div>
  <div class="hero-copy">
    <h1>Light Your Way Out Of Pain</h1>
    <p>Drug-free light therapy for lasting relief at home</p>
    <span class="btn btn-solid">Learn More</span>
  </div>
  <div class="tabs"><div class="tab">Drug-free</div><div class="tab">Safe</div><div class="tab">Pain relief</div></div>
</section>

<section class="how">
  <h2 class="section-title">How Light Therapy Can Stop Your Pain</h2>
  <div class="product-row">
    <span class="arrow" style="left:-30px">‹</span>
    <div class="product"><div class="product-img" role="img" aria-label="Light therapy device with case"></div><div class="product-name">Pro Light Package</div><div class="price">$379.00</div></div>
    <div class="product"><div class="product-img" role="img" aria-label="Red light therapy wand"></div><div class="product-name">Red Light · Home</div><div class="price">$249.00</div></div>
    <div class="product"><div class="product-img" role="img" aria-label="Green light therapy wand"></div><div class="product-name">Green Light · Home</div><div class="price">$249.00</div></div>
    <div class="product"><div class="product-img" role="img" aria-label="Violet light therapy wand"></div><div class="product-name">Violet Light · Home</div><div class="price">$249.00</div></div>
    <span class="arrow" style="right:-30px">›</span>
  </div>
</section>

<section class="testimonial">
  <h2 class="section-title">Testimonial</h2>
  <span class="t-arrow" style="left:200px">‹</span>
  <div class="quote-card">
    <div class="quote-side">
      <div class="avatar" role="img" aria-label="Portrait of the practitioner"></div>
      <div class="quote-name">Dr. Maren Holt</div>
      <div>Licensed acupuncturist and pain care practitioner for over twenty years</div>
    </div>
    <div class="quote-text">I have used these lights with my patients for years now and the results speak for themselves. People arrive in pain and leave moving freely. The lights are easy to use at home, safe for the whole family, and give relief without any drugs. I recommend them to every patient who lives with chronic pain and wants a gentle, natural option that truly works day after day.</div>
    <div class="stars">★★★★★</div>
  </div>
  <span class="t-arrow" style="right:200px">›</span>
</section>

<section class="pets">
  <h2 class="section-title">Light Therapy For <span>You</span> And <span>Your Pet</span></h2>
  <div class="pet-photos">
    <div style="flex:1.6;background:linear-gradient(135deg,#7a4c8c,#c78a8a)" role="img" aria-label="Two women smiling with a dog"></div>
    <div style="flex:1;background:linear-gradient(135deg,#4a4a55,#9a9aa4)" role="img" aria-label="Dog receiving light therapy"></div>
    <div style="flex:1;background:linear-gradient(135deg,#6a7e9a,#c7c7d0)" role="img" aria-label="Horse being treated with light"></div>
  </div>
</section>

<section class="featured">
  <h2 class="section-title">Featured Products</h2>
  <div class="product-row">
    <span class="arrow" style="left:-30px">‹</span>
    <div class="product"><div class="product-img" role="img" aria-label="Light therapy kit"></div><div class="product-name">Starter Light Kit</div><div class="price">$299.00</div></div>
    <div class="product"><div class="product-img" role="img" aria-label="Light therapy kit"></div><div class="product-name">Family Light Kit</div><div class="price">$349.00</div></div>
    <div class="product"><div class="product-img" role="img" aria-label="Light therapy kit"></div><div class="product-name">Pet Light Kit</div><div class="price">$279.00</div></div>
    <div class="product"><div class="product-img" role="img" aria-label="Light therapy kit"></div><div class="product-name">Pro Light Kit</div><div class="price">$399.00</div></div>
    <div class="product"><div class="product-img" role="img" aria-label="Light therapy kit"></div><div class="product-name">Travel Light Kit</div><div class="price">$229.00</div></div>
    <span class="arrow" style="right:-30px">›</span>
  </div>
</section>

<section class="story">
  <div class="story-text">
    <h3>The Brivontel Story – Short and Simple</h3>
    <div class="story-rule"></div>
    <p>Our founder found light therapy while searching for relief from years of pain. After seeing how well it worked, she began sharing the lights with friends, family and patients. Today we help thousands of people and their pets find relief at home. Every light is tested by our team, backed by years of hands-on care, and made to be easy and safe for anyone to use every day.</p>
  </div>
  <div class="story-photo" role="img" aria-label="Woman with a horse under a tree"></div>
</section>

<section class="blog">
  <h2 class="section-title">Our Blog</h2>
  <div class="blog-row">
    <div class="post"><div class="post-img" style="background:linear-gradient(135deg,#3a3a3a,#b0a890)" role="img" aria-label="Light being used on a hand"></div><div class="post-meta">June 2018</div><h4>Best Practices – Don't Forget</h4><p>Simple tips to get the most from every session with your light.</p></div>
    <div class="post"><div class="post-img" style="background:linear-gradient(180deg,#e8e8ee,#a8b4c8)" role="img" aria-label="Point guide software screenshot"></div><div class="post-meta">May 2018</div><h4>Point Guide Software on Sale</h4><p>Our reference software is on sale while quantities last.</p></div>
    <div class="post"><div class="post-img" style="background:linear-gradient(90deg,#1a1a2a,#c0307a,#30a0c0)" role="img" aria-label="Colourful lights glowing in the dark"></div><div class="post-meta">April 2018</div><h4>New Lights Coming</h4><p>A first look at the new colours joining our light family soon.</p></div>
  </div>
</section>

<section class="newsletter">
  <h2>Join Our Newsletter</h2>
  <div class="signup"><span class="field">Name</span><span class="field">Email</span><span class="btn">Submit</span></div>
</section>

<footer class="site-footer">brivontel.com</footer>
</body>
</html>
```